【テキスト】
ーーーーーーーーーーーーー
(メインタイトル)
黄金羅針盤アカデミー
実践攻略
前編
(サブタイトル)
相続市場を狙え!!
利回り20%&転売益2000万!
ーーーーーーーーーーーーー

【イメージ】
・3つ添付させて頂きました。
・「デザイン2」のように立体的にお願いします。
・文字は横書きでお願いします。

ターゲット:40~50代・男性・会社員:年収1000万
参考LP:https://veltrano-k.jp/lp/seminar1/

【納品形式】
PNGファイル
記載項目
(メインタイトル)
黄金羅針盤アカデミー
実践攻略
前編
(サブタイトル)
相続市場を狙え!!
利回り20%&転売益2000万!
サイズ
• 要相談・教えてください。
希望イメージ
シンプル 複雑
単色 カラフル
暗い 明るい
日常 高級
遊び心 厳粛
未来的 伝統的
女性的 男性的
希望する色
赤系、青系、紫系
納品ファイル
• PNG形式 (.png)
■ 選んだ理由

カラー・フォント・配置がバランス良く感じました。

■ 提案者全員のお礼・コメント

この度は大変お世話になりました。
別案件でまた依頼したいと感じました。

```html
<!DOCTYPE html>
<html lang="ja">
<head>
<meta charset="utf-8">
<title>黄金羅針盤アカデミー 実践攻略 前編</title>
<link rel="stylesheet" href="https://fonts.googleapis.com/css2?family=Noto+Sans+JP:wght@700;900&family=Noto+Serif+JP:wght@700;900&display=swap">
<style>
  :root {
    --navy: #1c1f5e;
    --navy-deep: #14174a;
    --ink: #111111;
    --white: #ffffff;
    --gold-light: #f6e3a6;
    --gold: #d4a94c;
    --gold-dark: #9c7429;
  }
  * { margin: 0; padding: 0; box-sizing: border-box; }
  html, body { width: 857px; height: 1200px; overflow: hidden; background: var(--white); }
  .cover {
    position: relative; width: 857px; height: 1200px;
    font-family: "Noto Sans JP", sans-serif; overflow: hidden;
    background: var(--white);
  }
  .series-tag {
    position: absolute; left: 220px; top: 0; width: 417px; height: 143px;
    background: var(--navy); color: var(--white);
    display: flex; align-items: center; justify-content: center;
    font-size: 80px; font-weight: 900; letter-spacing: 4px;
  }
  .title-line {
    position: absolute; font-weight: 900; line-height: 1; white-space: nowrap;
  }
  .title-top { left: 0; width: 857px; text-align: center; top: 228px; font-size: 140px; color: var(--ink); }
  .title-bottom { left: 48px; top: 408px; font-size: 130px; color: var(--navy); }
  .volume-mark {
    position: absolute; left: 710px; top: 412px; width: 64px; height: 142px;
    border: 5px solid var(--navy); color: var(--navy);
    display: flex; flex-direction: column; align-items: center; justify-content: center;
    font-size: 44px; font-weight: 900; line-height: 1.15;
  }
  .promo {
    position: absolute; left: 0; top: 600px; width: 857px; height: 600px;
    background: linear-gradient(180deg, var(--navy) 0%, var(--navy-deep) 100%);
  }
  .headline {
    position: absolute; top: 52px; left: 0; width: 857px; text-align: center;
    font-family: "Noto Serif JP", serif; font-weight: 900; white-space: nowrap;
    line-height: 1.1;
  }
  .headline-key {
    font-size: 90px;
    background: linear-gradient(180deg, var(--gold-light) 0%, var(--gold) 55%, var(--gold-dark) 100%);
    -webkit-background-clip: text; background-clip: text; color: transparent;
  }
  .headline-rest { font-size: 70px; color: var(--white); }
  .badge {
    position: absolute; top: 212px; width: 380px; height: 380px; border-radius: 50%;
    background: linear-gradient(160deg, var(--gold-light) 0%, var(--gold) 45%, var(--gold-dark) 100%);
    box-shadow: 0 10px 24px rgba(0,0,0,.45);
  }
  .badge-yield { left: 40px; }
  .badge-profit { left: 437px; }
  .badge-face {
    position: absolute; inset: 15px; border-radius: 50%;
    background: radial-gradient(circle at 40% 35%, #ffffff 0%, #f1f1f4 70%, #dcdce4 100%);
    display: flex; flex-direction: column; align-items: center; justify-content: center;
    font-family: "Noto Serif JP", serif; font-weight: 900; line-height: 1.1;
  }
  .badge-label { font-size: 74px; color: var(--ink); }
  .badge-figure {
    font-size: 82px; font-style: italic;
    background: linear-gradient(180deg, var(--gold) 0%, var(--gold-dark) 100%);
    -webkit-background-clip: text; background-clip: text; color: transparent;
  }
  .badge-unit { font-size: 40px; }
</style>
</head>
<body>
  <main class="cover">
    <div class="series-tag">実践攻略</div>
    <h1>
      <span class="title-line title-top">黄金羅針盤</span>
      <span class="title-line title-bottom">アカデミー</span>
    </h1>
    <div class="volume-mark"><span>前</span><span>編</span></div>

    <section class="promo">
      <p class="headline"><span class="headline-key">相続市場</span><span class="headline-rest">を狙え!!</span></p>
      <div class="badge badge-yield">
        <div class="badge-face">
          <span class="badge-label">利回り</span>
          <span class="badge-figure">20<span class="badge-unit">%</span></span>
        </div>
      </div>
      <div class="badge badge-profit">
        <div class="badge-face">
          <span class="badge-label">転売益</span>
          <span class="badge-figure">2000<span class="badge-unit">万</span></span>
        </div>
      </div>
    </section>
  </main>
</body>
</html>
```